Design a sharp Business Card, Stationary, and PowerPoint Template for Harbor Lantern Group (HLG)
Harbor Lantern Group (HLG) is a consulting firm with a mission
Professional
Maren Coleby Ashdown
Managing Director
4870 Larkspur Blvd. NW
Suite 2300
Washington, DC 20417
maren@harborlntn.example
www.harborlntn.example
I'm looking for something sharp that incorporates the colors of the logo.
Business card designs (only), please include this text:
We work with the military, private sector, and nonprofits to protect people affected by conflict and disaster.
This is the logo for Harbor Lantern Group (HLG). The black and red color combo is preferred.
For design purposes, the symbol can be used separately from the text and watermarked.

```html
<!DOCTYPE html>
<html lang="en">
<head>
<meta charset="utf-8">
<title>Harbor Lantern Group — Business Card</title>
<link rel="stylesheet" href="https://fonts.googleapis.com/css2?family=Montserrat:wght@300;400;600;700&display=swap">
<style>
  :root {
    --stage: #ffffff;
    --card-white: #ffffff;
    --card-shade: #ececec;
    --charcoal: #2e2e2e;
    --charcoal-deep: #242424;
    --swoosh-grey: #8c8c8c;
    --ink: #3a3a3a;
    --muted: #b9b9b9;
    --red: #d7262f;
    --white: #ffffff;
  }
  * { box-sizing: border-box; margin: 0; padding: 0; }
  html, body { width: 1200px; height: 980px; overflow: hidden; }
  body {
    background: var(--stage);
    font-family: "Montserrat", Arial, sans-serif;
    position: relative;
  }
  .card {
    position: absolute;
    width: 620px;
    height: 354px;
    border-radius: 22px;
    overflow: hidden;
    box-shadow: 0 2px 10px rgba(0,0,0,0.18);
  }

  /* Back card */
  .card-back {
    left: 530px; top: 70px;
    background: var(--charcoal);
    color: var(--white);
    text-align: center;
  }
  .card-back .brand {
    position: absolute; top: 96px; left: 0; right: 0;
    display: flex; align-items: center; justify-content: center; gap: 12px;
  }
  .brand-dot {
    width: 18px; height: 18px; border-radius: 50%;
    background: var(--red); flex: none;
  }
  .card-back .brand-name {
    font-weight: 300; font-size: 26px; letter-spacing: 3px;
    text-transform: uppercase; color: var(--white);
  }
  .mission {
    position: absolute; top: 186px; left: 0; right: 0;
    line-height: 1.5;
  }
  .mission .lead { font-size: 11px; color: var(--muted); font-weight: 400; }
  .mission .sectors { font-size: 12.5px; font-weight: 700; letter-spacing: 1px; color: var(--white); }
  .mission .close { font-size: 11px; color: var(--muted); font-weight: 400; }

  /* Front card */
  .card-front {
    left: 60px; top: 500px;
    background: radial-gradient(ellipse at 25% 30%, var(--card-white) 45%, var(--card-shade) 100%);
  }
  .card-front .sweep { position: absolute; inset: 0; }
  .card-front .brand {
    position: absolute; left: 322px; top: 40px;
    display: flex; align-items: flex-start; gap: 12px;
  }
  .card-front .brand-dot { margin-top: 6px; }
  .card-front .brand-name {
    font-weight: 300; font-size: 24px; letter-spacing: 5px; line-height: 1.3;
    text-transform: uppercase; color: var(--ink);
  }
  .contact {
    position: absolute; left: 38px; top: 60px;
    list-style: none; font-size: 11px; color: var(--ink); line-height: 1.75;
  }
  .contact li { display: flex; align-items: center; gap: 8px; }
  .contact .icon { width: 10px; height: 10px; flex: none; }
  .contact .spacer { width: 10px; flex: none; }
  .person {
    position: absolute; right: 40px; bottom: 36px; text-align right;
    text-align: right;
  }
  .person .name { color: var(--red); font-size: 13px; font-weight: 600; }
  .person .role { color: var(--white); font-size: 11px; font-weight: 400; margin-top: 4px; }
</style>
</head>
<body>

  <section class="card card-back" aria-label="Business card, back">
    <div class="brand">
      <span class="brand-dot"></span>
      <span class="brand-name">Harbor Lantern Group</span>
    </div>
    <div class="mission">
      <p class="lead">We work with the</p>
      <p class="sectors">MILITARY | PRIVATE SECTOR | NONPROFITS</p>
      <p class="close">to protect people affected by conflict and disaster.</p>
    </div>
  </section>

  <section class="card card-front" aria-label="Business card, front">
    <svg class="sweep" viewBox="0 0 620 354" width="620" height="354" aria-hidden="true">
      <path d="M620 60 C 560 190, 430 300, 200 354 L 620 354 Z" fill="var(--charcoal)"/>
      <path d="M620 38 C 556 172, 420 290, 170 354 L 184 354 C 428 294, 562 180, 620 48 Z" fill="var(--swoosh-grey)"/>
      <path d="M620 12 C 548 152, 400 280, 120 354 L 146 354 C 410 285, 554 162, 620 26 Z" fill="var(--charcoal-deep)"/>
    </svg>

    <div class="brand">
      <span class="brand-dot"></span>
      <span class="brand-name">Harbor<br>Lantern<br>Group</span>
    </div>

    <ul class="contact">
      <li>
        <svg class="icon" viewBox="0 0 10 10"><path d="M5 0.5a3.2 3.2 0 0 0-3.2 3.2C1.8 6 5 9.5 5 9.5S8.2 6 8.2 3.7A3.2 3.2 0 0 0 5 0.5Zm0 4.4a1.2 1.2 0 1 1 0-2.4 1.2 1.2 0 0 1 0 2.4Z" fill="var(--red)"/></svg>
        4870 Larkspur Blvd. NW
      </li>
      <li><span class="spacer"></span>Suite 2300 Washington, DC 20417</li>
      <li>
        <svg class="icon" viewBox="0 0 10 10"><path d="M2.2 0.8 3.8 2.6 3 3.8c.6 1.3 1.8 2.5 3.2 3.2l1.2-.8 1.8 1.6-.9 1.4C4.6 9 1 5.4.8 1.7Z" fill="var(--red)"/></svg>
        202-555-0148
      </li>
      <li>
        <svg class="icon" viewBox="0 0 10 10"><path d="M2.2 0.8 3.8 2.6 3 3.8c.6 1.3 1.8 2.5 3.2 3.2l1.2-.8 1.8 1.6-.9 1.4C4.6 9 1 5.4.8 1.7Z" fill="var(--red)"/></svg>
        202-555-0193
      </li>
      <li>
        <svg class="icon" viewBox="0 0 10 10"><rect x="0.5" y="2" width="9" height="6.5" fill="var(--red)"/><path d="M0.8 2.3 5 5.6 9.2 2.3" stroke="var(--white)" stroke-width="0.9" fill="none"/></svg>
        maren@harborlntn.example
      </li>
      <li>
        <svg class="icon" viewBox="0 0 10 10"><circle cx="5" cy="5" r="4.3" fill="none" stroke="var(--red)" stroke-width="1.1"/><path d="M0.8 5h8.4M5 0.7c-2.3 2.6-2.3 6 0 8.6M5 0.7c2.3 2.6 2.3 6 0 8.6" stroke="var(--red)" stroke-width="0.9" fill="none"/></svg>
        www.harborlntn.example
      </li>
    </ul>

    <div class="person">
      <p class="name">Maren Coleby Ashdown</p>
      <p class="role">Managing Director</p>
    </div>
  </section>

</body>
</html>
```